Female Vocalist with/Big Band Concert Marketing Package

Description

We would like to promote our Big Band Concert with a Nationally well known female Vocalist. She won the TV competition Fjellsang being Norways best artist of 2012 : http://www.kvorblad.no/scene/artikkel.php?artid=48213907

Size requirements :
Poster : A2 and A3
Flyer : 9x14 cm
Newspaper ad : Module 12B : 34 x 80 mm

Delivery file format :
PDFs in CMYK ready for printing
Must be editable in Illustrator CS6

Headlines :
Lene Holvik - main headline
m/Brekkvik Messingorkester - big band sharing the act
Messingkvelden - theme of this evening

Concert Dates, Venues and Web adresses :
27.april - Torvhaug Musikkhall - www.torvhaug-musikkhall.no
28.april - Brekkvik Kulturhus - www.brekkvik-kulturhus.no

Press Pictures and Graphics of artist and band :
May be used or not used according to design

Venue Logos :
There shall be a logo for each venue

Ticket sales logos :
There shall be a logo for each ticket sales office

Sponsors :
There must be a free field with room for sponsor logos

Link to graphics and logos :
https://www.filkassen.example/sh/q4lnzrwp8dyk2ha/mvTJ3uPq8x

```html
<!DOCTYPE html>
<html lang="no">
<head>
<meta charset="utf-8">
<title>Messingkvelden – Lene Holvik m/Brekkvik Messingorkester</title>
<link rel="stylesheet" href="https://fonts.googleapis.com/css2?family=PT+Sans:wght@400;700&family=PT+Sans+Narrow:wght@400;700&display=swap">
<style>
  :root {
    --ink: #000000;
    --paper: #ffffff;
    --amber: #f7a93b;
    --brass: #c9a36a;
    --gown: #1c2238;
    --stage-warm: #3a2a1c;
    --stage-dark: #120d09;
    --venue-blue: #1a8fd0;
    --venue-yellow: #f2c81a;
    --ticket-blue: #1e6fb8;
    --host-red: #d0262e;
  }
  * { margin: 0; padding: 0; box-sizing: border-box; }
  html, body { width: 848px; height: 1200px; overflow: hidden; background: var(--ink); }
  .poster {
    position: relative; width: 848px; height: 1200px; overflow: hidden;
    background: var(--ink); font-family: "PT Sans", sans-serif; color: var(--paper);
  }
  .photo { position: absolute; }
  .photo--band {
    left: 356px; top: 0; width: 492px; height: 645px;
    background: radial-gradient(ellipse at 60% 40%, #6b5238 0%, var(--stage-warm) 40%, var(--stage-dark) 100%);
  }
  .photo--guitar {
    left: 0; top: 0; width: 90px; height: 420px;
    background: linear-gradient(180deg, #4a3020 0%, #1a120c 100%);
  }
  .photo--drums {
    left: 310px; top: 205px; width: 170px; height: 215px;
    background: linear-gradient(160deg, #5a5a5a 0%, #1c1c1c 100%);
  }
  .photo--vocalist {
    left: 40px; top: 0; width: 330px; height: 952px;
    background: linear-gradient(180deg, #9c4a2a 0%, #6a3a2a 22%, var(--gown) 45%, #151a2c 100%);
    clip-path: polygon(18% 0, 64% 0, 68% 27%, 100% 34%, 100% 100%, 0 100%, 0 34%, 10% 27%);
  }
  .logo-field {
    position: absolute; left: 245px; top: 0; width: 230px; height: 205px; background: var(--ink); z-index: 1;
  }
  .band-mark {
    position: absolute; left: 268px; top: 62px; width: 200px; z-index: 2;
    font-family: "PT Sans", sans-serif; font-weight: 700; font-size: 25px; line-height: 1.1;
    color: var(--brass);
  }
  .theme {
    position: absolute; left: 95px; top: 652px;
    font-size: 37px; font-weight: 400; color: var(--paper);
  }
  .headline {
    position: absolute; left: 86px; top: 692px;
    font-size: 122px; font-weight: 400; line-height: 1; color: var(--amber); letter-spacing: -1px; white-space: nowrap;
  }
  .accolade {
    position: absolute; left: 0; width: 848px; top: 826px; text-align: center;
    font-size: 25px; font-weight: 700; color: var(--paper);
  }
  .guest-act {
    position: absolute; left: 0; width: 848px; top: 870px; text-align: center;
    font-family: "PT Sans Narrow", sans-serif; font-size: 32px; color: var(--amber);
  }
  .dates {
    position: absolute; left: 0; top: 953px; width: 848px; height: 153px; background: var(--paper);
  }
  .date-line {
    position: absolute; left: 40px;
    font-family: "PT Sans Narrow", sans-serif; font-size: 31px; color: var(--ink); white-space: nowrap;
  }
  .date-line--first { top: 22px; }
  .date-line--second { top: 88px; left: 43px; }
  .date-line .url { margin-left: 18px; }
  .venue-mark {
    position: absolute; left: 752px; width: 58px; text-align: center;
    font-size: 9px; font-weight: 700; line-height: 1.1; color: var(--ink);
  }
  .venue-mark .chip { display: block; width: 48px; height: 38px; margin: 0 auto 3px; }
  .venue-mark--first { top: 18px; }
  .venue-mark--first .chip { background: var(--venue-blue); }
  .venue-mark--second { top: 84px; }
  .venue-mark--second .chip { background: var(--venue-yellow); border-radius: 50%; width: 38px; }
  .sponsors {
    position: absolute; left: 0; top: 1106px; width: 848px; height: 94px; background: var(--ink);
  }
  .sponsor { position: absolute; font-weight: 700; white-space: nowrap; }
  .sponsor--tickets {
    left: 29px; top: 18px; width: 104px; height: 60px; border: 1px solid #888;
    font-size: 13px; color: var(--paper); padding: 20px 0 0 8px;
  }
  .sponsor--hotel {
    left: 340px; top: 30px; font-size: 24px; color: var(--host-red); display: flex; align-items: center; gap: 8px;
  }
  .sponsor--hotel .square { width: 18px; height: 18px; background: var(--host-red); }
  .sponsor--portal {
    left: 690px; top: 34px; font-size: 20px; color: var(--paper); display: flex; align-items: center; gap: 8px;
  }
  .sponsor--portal .dot { width: 22px; height: 22px; border-radius: 50%; background: var(--ticket-blue); }
</style>
</head>
<body>
<main class="poster">
  <div class="photo photo--guitar" role="img" aria-label="Guitarist on stage, cropped"></div>
  <div class="photo photo--band" role="img" aria-label="Big band brass section playing trombones on a dark stage"></div>
  <div class="photo photo--drums" role="img" aria-label="Drum kit on stage"></div>
  <div class="logo-field"></div>
  <div class="band-mark">Brekkvik<br>Messingorkester</div>
  <div class="photo photo--vocalist" role="img" aria-label="Red-haired female vocalist in a navy gown singing into a microphone with one arm outstretched"></div>

  <p class="theme">Messingkvelden</p>
  <h1 class="headline">Lene Holvik</h1>
  <p class="accolade">Norways best artist of 2012</p>
  <p class="guest-act">m/Brekkvik Messingorkester</p>

  <section class="dates">
    <p class="date-line date-line--first">27 April @ Torvhaug Musikkhall <span class="url">www.torvhaug-musikkhall.no</span></p>
    <p class="date-line date-line--second">28 April @ Brekkvik Kulturhus <span class="url">www.brekkvik-kulturhus.no</span></p>
    <div class="venue-mark venue-mark--first"><span class="chip"></span>TORVHAUG MUSIKKHALL</div>
    <div class="venue-mark venue-mark--second"><span class="chip"></span>BREKKVIK KULTURHUS</div>
  </section>

  <footer class="sponsors">
    <div class="sponsor sponsor--tickets">Billettkontoret</div>
    <div class="sponsor sponsor--hotel"><span class="square"></span>Kveldshotellet</div>
    <div class="sponsor sponsor--portal"><span class="dot"></span>Billettbua</div>
  </footer>
</main>
</body>
</html>
```